Cover for Where the Quiet River Bends Beyond Our Morning

Cover for a book that describes everything that happens to a person, from pre-birth life plans through growing in compassion and wisdom to death and living in the afterlife. The information is revealed in messages from people living in the life after this life. The title is Lanterns Along the Hidden Stair of Every Soul: Gathered from Voices Dwelling in the Further Meadow. Author is T. Morven Ashdale. Book size is 6 by 9.

Target Market(s)

General

Font styles to use
Serif

```html
<!DOCTYPE html>
<html lang="en">
<head>
<meta charset="utf-8">
<title>Lanterns Along the Hidden Stair of Every Soul — Cover</title>
<link href="https://fonts.googleapis.com/css2?family=Poppins:wght@600;700;800&display=swap" rel="stylesheet">
<style>
  :root {
    --page: #ffffff;
    --ink: #ffffff;
    --void: #05060a;
    --red: #c8221a;
    --orange: #e8611c;
    --yellow: #f2c021;
    --green: #2f9a34;
    --deep-blue: #141f6e;
    --blue: #1e8fd6;
  }
  html, body {
    margin: 0;
    width: 1200px;
    height: 1200px;
    overflow: hidden;
    background: var(--page);
  }
  .canvas {
    position: relative;
    width: 1200px;
    height: 1200px;
  }
  .cover {
    position: absolute;
    left: 233px;
    top: 50px;
    width: 734px;
    height: 1100px;
    overflow: hidden;
    font-family: "Poppins", sans-serif;
    color: var(--ink);
  }
  .cover-art {
    position: absolute;
    inset: 0;
    background:
      radial-gradient(ellipse 22% 17% at 50% 50%, var(--blue) 0%, var(--deep-blue) 55%, transparent 100%),
      radial-gradient(ellipse 40% 33% at 50% 52%, var(--void) 45%, var(--green) 72%, transparent 90%),
      radial-gradient(ellipse 58% 48% at 50% 52%, transparent 55%, var(--yellow) 72%, var(--orange) 86%, transparent 100%),
      linear-gradient(160deg, var(--red) 0%, #b81d1a 50%, var(--red) 100%);
  }
  .title-line {
    position: absolute;
    left: 0;
    right: 0;
    margin: 0;
    text-align: center;
    font-weight: 700;
    font-size: 50px;
    line-height: 1;
    letter-spacing: 0.5px;
    text-transform: uppercase;
  }
  .title-line--one { top: 302px; }
  .title-line--two { top: 367px; }
  .title-line--after { top: 718px; font-size: 54px; }
  .title-feature {
    position: absolute;
    left: 40px;
    top: 435px;
    width: 654px;
    height: 235px;
  }
  .subtitle {
    position: absolute;
    left: 0;
    right: 0;
    top: 832px;
    margin: 0;
    text-align: center;
    font-weight: 600;
    font-size: 23px;
    line-height: 1.2;
  }
  .author {
    position: absolute;
    left: 0;
    right: 0;
    top: 1010px;
    margin: 0;
    text-align: center;
    font-weight: 700;
    font-size: 30px;
  }
</style>
</head>
<body>
<main class="canvas">
  <section class="cover">
    <div class="cover-art" role="img" aria-label="Textured painting of nested frames in red, orange, yellow and green around a dark swirling blue vortex"></div>
    <h1 class="title-line title-line--one">Lanterns Along the</h1>
    <p class="title-line title-line--two">Hidden Stair of</p>
    <svg class="title-feature" viewBox="0 0 654 235" aria-label="Every">
      <text x="327" y="210" text-anchor="middle" textLength="640" lengthAdjust="spacingAndGlyphs"
            font-family="Poppins, sans-serif" font-weight="800" font-size="280"
            fill="#05060a" stroke="#ffffff" stroke-width="4" paint-order="fill">EVERY</text>
    </svg>
    <p class="title-line title-line--after">Soul</p>
    <p class="subtitle">Gathered from Voices Dwelling in the Further Meadow.</p>
    <p class="author">T. Morven Ashdale</p>
  </section>
</main>
</body>
</html>
```